Harbor Business Cards

I need a business card designed with the following information.

Company Name: Harbor Wealth Management
Name: BriAnne Dockery
Title: Executive Assistant
Cell: (281) 555-0173
Direct Line: (832) 555-0148
Email: brianne@harborwmx.com
Address: 20537 W. Marlowe PKWY Ste. B
Tomball, TX 77390

I have attached the logo.
I would like it in navy blue and silver.
Thanks.

```html
<!DOCTYPE html>
<html lang="en">
<head>
<meta charset="utf-8">
<title>Harbor Wealth Management — Business Card</title>
<link href="https://fonts.googleapis.com/css2?family=Montserrat:wght@300;400;700&display=swap" rel="stylesheet">
<style>
  :root {
    --navy: #10223f;
    --white: #ffffff;
    --stage: #4a4b4d;
    --ink-soft: #2a3a55;
  }
  * { box-sizing: border-box; margin: 0; padding: 0; }
  html, body { width: 1200px; height: 960px; overflow: hidden; }
  body {
    background: var(--stage);
    font-family: "Montserrat", Arial, sans-serif;
    position: relative;
  }
  .card {
    position: absolute;
    left: 250px;
    width: 700px;
    height: 400px;
    border-radius: 28px;
    overflow: hidden;
  }
  .card--back { top: 50px; background: var(--navy); }
  .card--front { top: 510px; background: var(--white); color: var(--navy); }

  .back-brand {
    position: absolute; inset: 0;
    display: flex; align-items: center; justify-content: center; gap: 14px;
    color: var(--white);
    font-weight: 400; font-size: 34px; letter-spacing: 10px; text-transform: uppercase;
  }
  .brand-square { width: 16px; height: 16px; background: var(--white); }

  .front-brand {
    position: absolute; left: 40px; top: 140px; width: 270px;
    display: flex; align-items: center; gap: 12px;
    color: var(--navy); text-transform: uppercase; font-weight: 400;
  }
  .brand-circle { flex: none; width: 16px; height: 16px; border-radius: 50%; background: var(--navy); }
  .front-brand__text { display: flex; flex-direction: column; gap: 8px; }
  .front-brand__name { font-size: 32px; letter-spacing: 10px; line-height: 1; }
  .front-brand__sub { font-size: 11px; letter-spacing: 3.4px; line-height: 1; white-space: nowrap; }

  .divider { position: absolute; left: 340px; top: 50px; width: 20px; height: 230px; }

  .contact { position: absolute; left: 390px; top: 62px; }
  .contact__name { font-weight: 700; font-size: 26px; }
  .contact__title { font-weight: 300; font-size: 20px; margin-top: 2px; color: var(--ink-soft); }
  .contact__list { list-style: none; margin-top: 28px; }
  .contact__item {
    display: flex; align-items: center; gap: 10px;
    font-weight: 400; font-size: 18px; line-height: 26px; color: var(--ink-soft);
  }
  .contact__item svg { width: 16px; height: 16px; flex: none; }

  .address-band {
    position: absolute; left: 0; right: 0; top: 322px; height: 44px;
    background: var(--navy); color: var(--white);
    display: flex; align-items: center; gap: 12px; padding-left: 24px;
    font-weight: 400; font-size: 17px;
  }
  .address-band svg { width: 18px; height: 22px; }
</style>
</head>
<body>

  <section class="card card--back" aria-label="Business card back">
    <div class="back-brand"><span class="brand-square"></span>Harbor</div>
  </section>

  <section class="card card--front" aria-label="Business card front">
    <div class="front-brand">
      <span class="brand-circle"></span>
      <div class="front-brand__text">
        <span class="front-brand__name">Harbor</span>
        <span class="front-brand__sub">Wealth Management</span>
      </div>
    </div>

    <svg class="divider" viewBox="0 0 20 230" aria-hidden="true">
      <g stroke="#10223f" stroke-width="2">
        <line x1="3" y1="0" x2="3" y2="230"/>
        <line x1="10" y1="0" x2="10" y2="230"/>
        <line x1="17" y1="0" x2="17" y2="230"/>
      </g>
    </svg>

    <div class="contact">
      <div class="contact__name">BriAnne Dockery</div>
      <div class="contact__title">Executive Assistant</div>
      <ul class="contact__list">
        <li class="contact__item">
          <svg viewBox="0 0 16 16" aria-hidden="true"><path fill="#10223f" d="M3.5 1.5l2.5 2.8-1.3 2a8 8 0 0 0 5 5l2-1.3 2.8 2.5-1.5 2.2C8 16 0 8 1.3 3z"/></svg>
          (281) 555-0173
        </li>
        <li class="contact__item">
          <svg viewBox="0 0 16 16" aria-hidden="true"><rect x="4" y="1" width="8" height="14" rx="1.5" fill="none" stroke="#10223f" stroke-width="1.6"/><circle cx="8" cy="12.5" r="0.9" fill="#10223f"/></svg>
          (832) 555-0148
        </li>
        <li class="contact__item">
          <svg viewBox="0 0 16 16" aria-hidden="true"><rect x="1" y="3" width="14" height="10" fill="#10223f"/><path d="M1 3l7 6 7-6" fill="none" stroke="#fff" stroke-width="1.2"/></svg>
          brianne@harborwmx.com
        </li>
      </ul>
    </div>

    <div class="address-band">
      <svg viewBox="0 0 18 22" aria-hidden="true"><path fill="#fff" d="M9 0a8 8 0 0 1 8 8c0 6-8 14-8 14S1 14 1 8a8 8 0 0 1 8-8z"/><circle cx="9" cy="8" r="3" fill="#10223f"/></svg>
      20537 W. Marlowe PKWY Ste. B, Tomball, TX 77390
    </div>
  </section>

</body>
</html>
```